VARNO HOMES BRELT MARKETING FLYER

THE FLYER CAN BE FRONT TO BACK OR 2 PAGES IF NEEDED.

need to create a flyer with the following information:

Tallwick Co. is a CRM (Customer Relationship Management System) that provides leads to agents and a system to communicate and track your leads. Initial training and set up will be provided

Commission splits for leads are as follows: (maybe we can create a chart or box for items 1-3)

1. Cold leads 40% Varno - 60% Agent - Worked by Agent in the platform, agent shows property, writes contract, handles all negotiations and any necessary addendums, attends home inspection and settlement.

2. Warm leads 50% Varno - 50% Co-agent - Contacted by ISA, agent shows property, writes contract, handles all negotiations and any necessary addendums, attends home inspection and settlement.

3 Hot leads 70% Varno - 30% Co-agent - Prequalified by Varno Homes and ready to look at property, Varno writes contract and secures broker agency relationship agreements, co-agent shows property, , handles all negotiations (with support from VARNO if necessary), execute any necessary addendums, attend home inspection and settlement.

Preferred vendors such as Lender, Title, Insurance, Home Inspector, etc. are to be used for any transactions related to BRLT per Varno Homes.

Agents will receive 10 leads for free to start once Fresh Member Launchpad is complete. Warm leads will be available to purchase for $15 each beyond the first 10. Every 5 deals closed, agent commission will increase by 10% annually!!

Rules and restrictions apply.

3. In addition to Pennvale, a transaction coordinator included.

4. Free BRLT Support and training included

5. Free personal CRM website included

Industry/Entity Type

Real Estate

Colors
3176b5
85abd2
ecf5f6

Requirements
Must have
• everything in the description above

```html
<!DOCTYPE html>
<html lang="en">
<head>
<meta charset="utf-8">
<title>Varno Homes BRLT Flyer</title>
<link href="https://fonts.googleapis.com/css2?family=Montserrat:wght@300;400;500;600;700;800;900&display=swap" rel="stylesheet">
<style>
  :root {
    --stage: #cdcfd1;
    --teal: #0a86a8;
    --teal-text: #1589ad;
    --green: #22ad8c;
    --page-light: #ecece6;
    --ink: #3d3d3d;
    --card: #eeeeee;
    --card-strip: #cfcfcf;
    --navy: #24356f;
    --brand-blue: #3176b5;
  }
  * { box-sizing: border-box; margin: 0; padding: 0; }
  html, body { width: 1200px; height: 947px; overflow: hidden; }
  body { background: var(--stage); font-family: "Montserrat", sans-serif; position: relative; }

  .page { position: absolute; top: 171px; width: 429px; height: 607px; overflow: hidden; }
  .page--front { left: 158px; background: var(--page-light); }
  .page--back { left: 613px; background: var(--teal); }

  /* front */
  .hero-photo { position: absolute; left: 0; top: 0; width: 429px; height: 377px;
    background: linear-gradient(160deg, #f4f2ef 0%, #e9e4df 40%, #d9d3cc 75%, #c9b9aa 100%); }
  .brand-mark { position: absolute; left: 20px; top: 24px; display: flex; align-items: center; gap: 8px; }
  .brand-mark__square { width: 16px; height: 16px; background: var(--green); }
  .brand-mark__name { font-size: 44px; font-weight: 500; color: #4a4a4a; letter-spacing: 1px; line-height: 1; }

  .front-headline { position: absolute; left: 0; width: 429px; top: 381px; text-align: center;
    color: var(--teal-text); font-weight: 900; font-size: 15.5px; line-height: 18px; }
  .front-body { position: absolute; left: 0; width: 429px; top: 415px; text-align: center;
    color: #555; font-weight: 300; font-size: 15.6px; line-height: 18.3px; }
  .front-rule { position: absolute; left: 104px; top: 498px; width: 221px; height: 7px; background: var(--green); }
  .perks { position: absolute; top: 528px; left: 82px; display: flex; gap: 28px; }
  .perk { display: flex; align-items: center; gap: 9px; }
  .perk__text { color: var(--teal-text); font-weight: 700; font-size: 9.8px; line-height: 12px; }
  .front-band { position: absolute; left: 0; bottom: 0; width: 429px; height: 9px; background: var(--green); }

  /* back */
  .splits-title { position: absolute; left: 52px; top: 49px; color: #fff; font-weight: 800; font-size: 12.6px; letter-spacing: .1px; }
  .lead-card { position: absolute; left: 52px; width: 328px; height: 96px; background: var(--card);
    border-bottom: 6px solid var(--card-strip); }
  .lead-card--cold { top: 75px; }
  .lead-card--warm { top: 190px; }
  .lead-card--hot { top: 307px; }
  .lead-tag { position: absolute; left: 0; top: 0; height: 20px; padding: 0 30px 0 9px; display: flex; align-items: center;
    color: #fff; font-size: 8.4px; border-radius: 0 0 14px 0; white-space: nowrap; }
  .lead-tag b { font-weight: 800; margin-right: 2px; }
  .lead-card--cold .lead-tag { background: linear-gradient(90deg, #0c78aa, #17c4e0); }
  .lead-card--warm .lead-tag { background: linear-gradient(90deg, #f05a1e, #f7b51a 85%, #f9d21b); }
  .lead-card--hot .lead-tag { background: linear-gradient(90deg, #e41e26, #f0511e 50%, #f7941d); }
  .lead-list { position: absolute; top: 30px; left: 14px; right: 10px; display: grid; grid-template-columns: 150px 150px; column-gap: 0; row-gap: 6px; list-style: none; }
  .lead-list li { position: relative; padding-left: 10px; font-size: 6.2px; font-weight: 600; color: var(--ink); line-height: 7.4px; }
  .lead-list li::before { content: ""; position: absolute; left: 0; top: 1px; width: 3px; height: 5px;
    border: solid var(--tick); border-width: 0 1.5px 1.5px 0; transform: rotate(40deg); }
  .lead-card--cold { --tick: #1a9fd0; }
  .lead-card--warm { --tick: #f39a1c; }
  .lead-card--hot { --tick: #e8352a; }

  .divider { position: absolute; left: 49px; top: 426px; width: 332px; border-top: 1px dashed rgba(255,255,255,.45); }
  .notes { position: absolute; left: 53px; top: 449px; display: flex; gap: 12px; }
  .note { color: #fff; font-size: 6.9px; line-height: 9.4px; font-weight: 400; }
  .note--vendors { width: 112px; padding-right: 0; }
  .note--leads { width: 190px; padding-left: 12px; border-left: 3px solid rgba(255,255,255,.35); }
  .note b { font-weight: 700; }
  .fine-print { position: absolute; left: 0; width: 429px; top: 514px; text-align: center; color: #fff; font-size: 4.6px; letter-spacing: 1.3px; font-weight: 500; }
  .partner-bar { position: absolute; left: 0; bottom: 0; width: 429px; height: 78px; background: #fff;
    display: flex; align-items: center; justify-content: center; gap: 32px; }
  .partner { display: flex; align-items: center; gap: 6px; }
  .partner__square { width: 12px; height: 12px; background: var(--navy); }
  .partner__name { color: var(--navy); font-weight: 600; font-size: 13px; letter-spacing: .5px; }
  .partner--second .partner__square { background: var(--brand-blue); border-radius: 50%; }
  .partner--second .partner__name { color: var(--brand-blue); font-size: 9px; }
</style>
</head>
<body>

<section class="page page--front">
  <div class="hero-photo" role="img" aria-label="Photo of a handshake over a desk with a small wooden house model, keys, papers and a phone"></div>
  <div class="brand-mark">
    <span class="brand-mark__square"></span>
    <span class="brand-mark__name">BRLT</span>
  </div>
  <h1 class="front-headline">BRLT TAKES THE GUESSWORK<br>OUT OF GENERATING LEADS</h1>
  <p class="front-body">and effectively moving them<br>through the homebuyer and seller<br>journey, so you have more time to<br>focus on growing your business.</p>
  <div class="front-rule"></div>
  <div class="perks">
    <div class="perk">
      <svg width="48" height="46" viewBox="0 0 48 46" fill="none" stroke="#1589ad" stroke-width="2">
        <rect x="2" y="2" width="44" height="30" rx="2"/>
        <rect x="6" y="6" width="36" height="22"/>
        <rect x="11" y="10" width="20" height="12"/>
        <line x1="14" y1="16" x2="24" y2="16"/>
        <path d="M29 17 l8 3 -3 2 3 3 -2 2 -3-3 -2 3z" fill="#fff"/>
        <path d="M20 32 v7 M28 32 v7 M13 42 h22"/>
      </svg>
      <span class="perk__text">Free<br>personal<br>CRM website</span>
    </div>
    <div class="perk">
      <svg width="46" height="46" viewBox="0 0 46 46" fill="none" stroke="#1589ad" stroke-width="2">
        <path d="M9 22 a14 14 0 0 1 28 0"/>
        <rect x="6" y="20" width="6" height="10" rx="2"/>
        <rect x="34" y="20" width="6" height="10" rx="2"/>
        <path d="M37 30 q0 6 -9 7"/>
        <circle cx="26" cy="37" r="2"/>
        <path d="M4 45 q2-8 19-8 q17 0 19 8"/>
      </svg>
      <span class="perk__text">Free BRLT<br>Support<br>and training</span>
    </div>
  </div>
  <div class="front-band"></div>
</section>

<section class="page page--back">
  <h2 class="splits-title">COMMISSION SPLITS FOR LEADS ARE AS FOLLOWS:</h2>

  <div class="lead-card lead-card--cold">
    <div class="lead-tag"><b>COLD LEADS</b>&nbsp;| 40% Varno - 60% Agent</div>
    <ul class="lead-list">
      <li>Worked by agent in the platform</li>
      <li>Agent writes contract</li>
      <li>Agent shows property</li>
      <li>Attends home inspection and settlement.</li>
      <li>Handles all negotiations and any necessary addendums</li>
    </ul>
  </div>

  <div class="lead-card lead-card--warm">
    <div class="lead-tag"><b>WARM LEADS</b>&nbsp;| 50% Varno - 50% Co-Agent</div>
    <ul class="lead-list">
      <li>Contacted by ISA</li>
      <li>Agent writes contract</li>
      <li>Agent shows property</li>
      <li>Agent attends home inspection and settlement.</li>
      <li>Agent handles all negotiations and any necessary addendums</li>
    </ul>
  </div>

  <div class="lead-card lead-card--hot">
    <div class="lead-tag"><b>HOT LEADS</b>&nbsp;| 70% Varno - 30% Co-Agent</div>
    <ul class="lead-list">
      <li>Prequalified by Varno Homes and ready to look at property</li>
      <li>Co-agent handles all negotiations (with support from Varno if necessary)</li>
      <li>Varno writes contract and secures broker agency relationship agreements</li>
      <li>Co-agent execute any necessary addendums, attend home inspection and settlement.</li>
      <li>Co-agent shows property</li>
    </ul>
  </div>

  <div class="divider"></div>
  <div class="notes">
    <p class="note note--vendors">Preferred vendors such as Lender, Title, Insurance, Home Inspector, etc. are to be used for any transactions related to BRLT per Varno Homes.</p>
    <p class="note note--leads">Agents will receive <b>10 leads for free to start</b> once Fresh Member Launchpad is complete. Warm leads will be available to purchase for $15 each beyond the first 10. Every 5 deals closed, agent commission will increase by 10% annually!!</p>
  </div>
  <p class="fine-print">*RULES AND RESTRICTIONS APPLY.</p>

  <div class="partner-bar">
    <div class="partner"><span class="partner__square"></span><span class="partner__name">VARNO HOMES</span></div>
    <div class="partner partner--second"><span class="partner__square"></span><span class="partner__name">Halden Realty Group</span></div>
  </div>
</section>

</body>
</html>
```